verdant terraces simple classy business card design

my name is owen harlow and I run a gardening business aimed at high class verdant terraces. the business name is verdant terraces and our logo was designed on pixel forum .My clientel are anything from residential homes to businesses. I take pride in my work and know that I offer a service like no other in my area.
The business card will be used to represent my business and I want it to be not only rememberable, but simplistic and modern. Eye catching too. Of course I would like it relatable to gardening and appealing to the correct clientel - those being garden enthusiasts, prestigious homes and businesses that are after top of the line gardening services like no other on the market.
I am not a typical lawn mowing business so I don't want a typical card design that represents that. The gardens I work with are generally million dollar properties with owners who are very garden proud looking for upkeep and guidance from me along with sometimes whole new garden designs. I want the business cards to show to my clients that I take pride, as they do, in their garden. And I want them to know from my card that I am a professional, qualified horticulturist offering them a top of the line service for life. I want them to refer my business on. I want them to look at my business card and see class and professionalism in a modern unique bold way.
The card should be simple with the possibility of the logo on the front being embossed/debossed and my details on the back the card should have a organic garden feel it's very important to me that it is absolutely perfect
I am also very open to ideas and suggestions so look forward to seeing the designs. the business logo has been supplied with this project and I want the card to be double sided

Contact info is
Owen Harlow - Managing Director / Horticulturist
Phone : 0481 526 704
Email: owenharlow@verdantterraces.com.au

Target Market(s)

high class gardens residential and commercial

Industry/Entity Type

Gardener

Contact Information for Business Card

Contact info is
Phone : 0481 526 704

PLEASE MAKE CARD DOUBLE SIDED

Requirements
Must have
• organic simple classy modern feel
• must flow with the current logo that has been supplied with this project
• Double sided
• Must explain in a simple way that I deal with high end gardens and I'm a qualified horticulturist
Nice to have
• embossed debossed logo
Should not have
• shouldn't be to busy or cheap looking

```html
<!DOCTYPE html>
<html lang="en">
<head>
<meta charset="utf-8">
<title>Verdant Terraces — Business Card</title>
<link rel="stylesheet" href="https://fonts.googleapis.com/css2?family=Arimo:wght@400;700&display=swap">
<style>
  :root {
    --backdrop: #ece6dd;
    --leaf-green: #4e9a45;
    --card-white: #fbfbf9;
    --ink: #3a3a3a;
    --on-green: #ffffff;
    --shadow: rgba(60, 45, 30, 0.18);
  }
  * { margin: 0; padding: 0; box-sizing: border-box; }
  html, body {
    width: 1200px;
    height: 794px;
    overflow: hidden;
    background: var(--backdrop);
    font-family: "Arimo", Arial, sans-serif;
  }
  .canvas {
    position: relative;
    width: 1200px;
    height: 794px;
  }
  .card {
    position: absolute;
    top: 242px;
    width: 540px;
    height: 310px;
    box-shadow: 0 6px 18px var(--shadow);
  }
  /* Front side */
  .card-front {
    left: 45px;
    background: var(--leaf-green);
    color: var(--on-green);
  }
  .front-brand {
    position: absolute;
    top: 96px;
    left: 0;
    right: 0;
    display: flex;
    flex-direction: column;
    align-items: center;
    gap: 16px;
  }
  .brand-dot {
    width: 44px;
    height: 44px;
    border-radius: 50%;
    background: var(--on-green);
  }
  .front-brand .brand-name {
    font-size: 24px;
    font-weight: 700;
    letter-spacing: 5px;
    text-transform: uppercase;
    color: var(--on-green);
  }
  .front-website {
    position: absolute;
    bottom: 30px;
    left: 0;
    right: 0;
    text-align: center;
    font-size: 13px;
    letter-spacing: 2.4px;
  }
  /* Back side */
  .card-back {
    left: 615px;
    background: var(--card-white);
    color: var(--ink);
  }
  .back-brand {
    position: absolute;
    top: 40px;
    right: 36px;
    display: flex;
    align-items: center;
    gap: 12px;
  }
  .back-brand .brand-dot {
    width: 26px;
    height: 26px;
    background: var(--leaf-green);
  }
  .back-brand .brand-name {
    font-size: 22px;
    font-weight: 700;
    letter-spacing: 3px;
    text-transform: uppercase;
    color: var(--leaf-green);
  }
  .contact {
    position: absolute;
    left: 36px;
    bottom: 34px;
    font-size: 13.5px;
    line-height: 1.55;
  }
  .contact-name {
    font-size: 19px;
    font-weight: 700;
    color: var(--leaf-green);
    line-height: 1.3;
  }
  .contact-role { margin-bottom: 8px; }
  .contact-label {
    font-weight: 700;
    color: var(--leaf-green);
    margin-right: 4px;
  }
</style>
</head>
<body>
  <main class="canvas">
    <section class="card card-front" aria-label="Card front">
      <div class="front-brand">
        <span class="brand-dot"></span>
        <span class="brand-name">Verdant Terraces</span>
      </div>
      <p class="front-website">www.verdantterraces.com.au</p>
    </section>

    <section class="card card-back" aria-label="Card back">
      <div class="back-brand">
        <span class="brand-dot"></span>
        <span class="brand-name">Verdant Terraces</span>
      </div>
      <div class="contact">
        <p class="contact-name">Owen Harlow</p>
        <p class="contact-role">Managing Director / Horticulturist</p>
        <p class="contact-phone"><span class="contact-label">P :</span>0481 526 704</p>
        <p class="contact-email">owenharlow@verdantterraces.com.au</p>
        <p class="contact-web">verdantterraces.com.au</p>
      </div>
    </section>
  </main>
</body>
</html>
```